ALL TEXT Social Media Graphics

We are looking for a series of social media graphics for Instagram (new size: 4:5 (1080 x 1350 pixels) ratio that are ALL TEXT. We want the following quotes below on each graphic; one quote per graphic. AND, In very small letters at the bottom of each graphic, add @PaulaWrenLive
The look and feel of these graphics should be complimentary to the color palette attached below; but keep them simple. But the design is up to you; at the end of this document, I provided various samples of all text graphics that I like as examples.
The Quotes are in the attached WORD document
women trying to lose weight

```html
<!DOCTYPE html>
<html lang="en">
<head>
<meta charset="utf-8">
<title>Golden Summer Slimdown – Social Graphics</title>
<link rel="stylesheet" href="https://fonts.googleapis.com/css2?family=Roboto:ital,wght@0,300;0,400;0,500;0,700;1,300;1,400;1,500;1,700;1,900&display=swap">
<style>
  :root{
    --magenta:#a8114f;
    --magenta-deep:#b3155a;
    --rose:#e25d9a;
    --hot-pink:#ec5b9b;
    --blush:#fcc4e3;
    --blush-deep:#f7b3d8;
    --petal:#f08cb6;
    --paper:#ffffff;
    --ink:#1a1a1a;
    --stage:#f7d3e1;
  }
  *{box-sizing:border-box;margin:0;padding:0}
  html,body{width:1200px;height:1200px;overflow:hidden}
  body{
    font-family:"Roboto",Arial,sans-serif;
    background:
      radial-gradient(circle at 20% 15%,rgba(255,255,255,.7),transparent 40%),
      radial-gradient(circle at 85% 80%,rgba(255,255,255,.6),transparent 45%),
      radial-gradient(circle at 60% 40%,#f3bfd4,transparent 60%),
      var(--stage);
    position:relative;
  }
  .post{position:absolute;width:352px;height:440px;overflow:hidden;box-shadow:0 2px 8px rgba(150,40,90,.15)}
  .row-1{top:142px}.row-2{top:619px}
  .col-1{left:42px}.col-2{left:424px}.col-3{left:807px}
  .abs{position:absolute}
  .photo{position:absolute}
  .handle{position:absolute;font-size:11px;font-weight:700}
  .b{font-weight:700}

  /* Post 1 */
  .post-system{background:linear-gradient(180deg,#e56aa3 0%,#c52f70 55%,var(--magenta-deep) 100%)}
  .post-system .halo{left:-25px;top:108px;width:210px;height:210px;border-radius:50%;background:#f3a6cb}
  .post-system .photo{left:14px;top:24px;width:150px;height:296px;border-radius:70px 70px 40px 40px;background:linear-gradient(180deg,#3b3340,#1f3a66 55%,#161616)}
  .post-system .pitch{right:10px;top:96px;text-align:right;font-style:italic;font-size:20px;line-height:22px;color:#fde6f1}
  .post-system .pitch strong{color:var(--magenta);font-weight:700;font-size:21px}
  .post-system .pitch .soft{color:#f9c2dc;font-weight:400;font-size:17px;line-height:20px}
  .post-system .pitch .cta{font-size:16px;line-height:21px;color:#fff}
  .post-system .pitch .cta .key{color:var(--ink);font-weight:700;font-style:normal}
  .post-system .offer{left:12px;top:338px;font-size:18px;line-height:23px;color:#fff;font-style:italic}
  .post-system .offer .dark{color:var(--ink);font-style:normal;font-weight:500}
  .post-system .handle{left:12px;top:414px;color:#fff}

  /* Post 2 */
  .post-notover{background:var(--paper)}
  .post-notover .photo{left:21px;top:116px;width:109px;height:298px;border-radius:12px 12px 0 0;background:linear-gradient(180deg,var(--magenta) 0%,#6e5a68 45%,#a9c3de 100%)}
  .post-notover .headline{right:20px;top:82px;text-align:right;font-style:italic;color:var(--magenta);font-size:17px;line-height:21px;font-weight:300}
  .post-notover .headline .big{font-weight:900;font-size:21px;line-height:22px}
  .post-notover .pill{left:109px;top:272px;width:217px;height:30px;border-radius:0 15px 15px 0;background:var(--magenta);color:#fff;font-style:italic;font-size:14px;text-align:right;padding:6px 14px 0 0}
  .post-notover .follow{right:19px;top:312px;text-align:right;font-style:italic;font-size:17px;line-height:20px;color:var(--magenta);font-weight:300}
  .post-notover .follow b{font-weight:700}
  .post-notover .band{left:0;top:413px;width:352px;height:27px;background:var(--blush)}
  .post-notover .handle{right:20px;top:418px;font-size:13px;font-weight:400;font-style:italic;color:var(--magenta)}

  /* Post 3 */
  .post-down{background:var(--blush-deep)}
  .post-down .corner{right:0;top:47px}
  .post-down .lead{left:11px;top:83px;font-size:19px;line-height:21px;font-style:italic;font-weight:300;color:var(--ink)}
  .post-down .lead b{color:var(--magenta);font-weight:700}
  .post-down .photo{
    left:172px;top:160px;width:180px;height:280px;
    background:linear-gradient(180deg,#2a1c1c 0%,#8a5a45 35%,#d7262f 62%,#c01f29 100%);
    clip-path:polygon(38% 0,100% 0,100% 100%,0 100%,0 32%,38% 32%);
  }
  .post-down .cta{left:11px;top:300px;font-size:17px;line-height:20px;font-style:italic;color:var(--ink)}
  .post-down .cta .mag{color:var(--magenta)}
  .post-down .handle{left:10px;top:418px;color:var(--ink)}

  /* Post 4 */
  .post-waist{background:linear-gradient(160deg,#ffffff 0%,#fdf0f5 55%,#fbe3ee 100%)}
  .post-waist .quote{left:28px;top:86px;text-transform:uppercase;font-style:italic;font-weight:300;font-size:21px;line-height:26px;color:var(--ink)}
  .post-waist .quote .pk{color:var(--hot-pink);font-weight:700}
  .post-waist .quote .pkl{color:var(--hot-pink)}
  .post-waist .cta{left:32px;top:282px;text-transform:uppercase;font-style:italic;font-weight:300;font-size:18px;line-height:22px;color:var(--ink)}
  .post-waist .cta b{font-weight:700}
  .post-waist .cta .pk{color:var(--hot-pink);font-weight:700}
  .post-waist .handle{right:22px;top:408px;color:var(--hot-pink);font-weight:400;font-size:11px}

  /* Post 5 */
  .post-sis{background:linear-gradient(180deg,#fdf1f6 0%,#fbe2ec 100%)}
  .post-sis .quote{left:22px;top:68px;text-transform:uppercase;font-style:italic;font-weight:300;font-size:30px;line-height:32px;color:var(--ink)}
  .post-sis .quote .mag{color:var(--magenta);font-weight:900}
  .post-sis .quote .magl{color:var(--magenta)}
  .post-sis .cta{left:22px;top:287px;text-transform:uppercase;font-style:italic;font-weight:300;font-size:18px;line-height:21px;color:var(--magenta)}
  .post-sis .cta .dark{color:var(--ink);font-weight:700}
  .post-sis .cta .key{color:var(--magenta)}
  .post-sis .handle{right:22px;top:408px;color:var(--magenta);font-weight:700}

  /* Post 6 */
  .post-time{background:var(--paper)}
  .post-time .shapes{left:0;top:0}
  .post-time .quote{left:82px;top:104px;text-transform:uppercase;font-size:20px;line-height:27px;color:var(--magenta);font-weight:400}
  .post-time .quote b{font-weight:700}
  .post-time .pill{left:0;top:309px;width:162px;height:58px;border-radius:0 29px 29px 0;background:var(--magenta);color:#fff;font-style:italic;font-size:15px;line-height:18px;padding:11px 0 0 33px;text-transform:uppercase;font-weight:300}
  .post-time .pill b{font-weight:700}
  .post-time .handle{right:22px;top:410px;color:#fff;font-weight:400}
</style>
</head>
<body>

<section class="post post-system row-1 col-1">
  <svg class="abs" width="352" height="440" style="left:0;top:0">
    <circle cx="272" cy="-22" r="80" fill="none" stroke="#a8114f" stroke-width="13"/>
  </svg>
  <div class="abs halo"></div>
  <div class="photo" role="img" aria-label="Smiling woman in a denim jacket holding a glass of green juice"></div>
  <p class="abs pitch">
    <strong>You don't need<br>another diet.</strong><br>
    <span class="soft">You need a system<br>that works.</span><br>
    <span class="cta b">Comment ;</span><br>
    <span class="cta"><span class="key">“Summer”</span><br>to start now.</span>
  </p>
  <p class="abs offer"><b>Drop 30 pounds</b> with the<br><span class="dark">Golden Summer Slimdown.</span></p>
  <span class="handle">@PaulaWrenLive</span>
</section>

<section class="post post-notover row-1 col-2">
  <div class="photo" role="img" aria-label="Smiling woman in a grey crop top and jeans, hand on hip"></div>
  <p class="abs headline">
    <span class="big">THIS SUMMER</span><br>
    <span class="big">ain't OVER</span> and<br>
    neither are your<br>
    body goals. Drop<br>
    <b>30 POUNDS</b> with<br>
    the <b>Golden Summer</b><br>
    <b>Slimdown.</b>
  </p>
  <div class="abs pill">Comment;</div>
  <p class="abs follow"><b>“Hot Girl”</b><br>to get the plan</p>
  <div class="abs band"></div>
  <span class="handle">@PaulaWrenLive</span>
</section>

<section class="post post-down row-1 col-3">
  <svg class="abs corner" width="148" height="122">
    <polygon points="0,0 148,0 148,122" fill="#f08cb6"/>
  </svg>
  <p class="abs lead">
    You can absolutely<br>
    be <b>Down 20–30 Pounds</b><br>
    by end of summer.<br>
    All it takes is the<br>
    right plan and you've<br>
    found it.
  </p>
  <div class="photo" role="img" aria-label="Smiling woman in a red crop top pointing to the side"></div>
  <p class="abs cta">
    <b>Comment ;</b><br>
    <b class="mag">“Hot Girl”</b><br>
    <span class="mag">for the</span><br>
    <b class="mag">Golden Summer<br>Slimdown!</b>
  </p>
  <span class="handle">@PaulaWrenLive</span>
</section>

<section class="post post-waist row-2 col-1">
  <p class="abs quote">
    <span class="pk">Snatched waist,</span><br>
    <span class="pk">flat tummy,</span><br>
    30 pounds lighter<br>
    that's what the <span class="pkl">Golden</span><br>
    <span class="pkl">Summer Slimdown</span><br>
    <span class="pk">challenge delivers.</span>
  </p>
  <p class="abs cta">
    <b>Comment;</b><br>
    <span class="pk">“Hot Girl”</span> to get<br>
    the plan
  </p>
  <span class="handle">@PAULAWRENLIVE</span>
</section>

<section class="post post-sis row-2 col-2">
  <p class="abs quote">
    <span class="magl">Sis,</span><br>
    We're <span class="mag">dropping</span><br>
    <span class="mag">belly flat</span> and<br>
    saying <span class="mag">goodbye</span><br>
    to <span class="mag">stubborn</span><br>
    <span class="mag">pounds.</span>
  </p>
  <p class="abs cta">
    <span class="dark">Comment <span class="key">“Summer”</span>!</span><br>
    to join the Golden<br>
    Summer Slimdown
  </p>
  <span class="handle">@PAULAWRENLIVE</span>
</section>

<section class="post post-time row-2 col-3">
  <svg class="abs shapes" width="352" height="440">
    <defs>
      <linearGradient id="fade-top" x1="0" y1="0" x2="1" y2="1">
        <stop offset="0" stop-color="#b3155a"/>
        <stop offset="1" stop-color="#e98bb6"/>
      </linearGradient>
      <linearGradient id="fade-bottom" x1="1" y1="1" x2="0" y2="0">
        <stop offset="0" stop-color="#b3155a"/>
        <stop offset="1" stop-color="#f4b7d3"/>
      </linearGradient>
    </defs>
    <polygon points="0,0 171,0 0,181" fill="url(#fade-top)"/>
    <polygon points="352,292 352,440 188,440" fill="url(#fade-bottom)"/>
  </svg>
  <p class="abs quote">
    There's still <b>time</b><br>
    <b>to drop</b> the<br>
    <b>30 pounds</b> and<br>
    slay this summer.<br>
    The Golden<br>
    Summer Slimdown<br>
    has the <b>blueprint.</b>
  </p>
  <div class="abs pill">Comment;<br><b>“Hot Girl”!</b></div>
  <span class="handle">@PAULAWRENLIVE</span>
</section>

</body>
</html>
```